Carpentry framing business card and logo design

We need a logo that works well with baseball caps, tee shirts and sweat shirts. We are a carpentry framing company specializing in apartment complexes and large residential communities. We work in what is known as the tri state area southeastern Pennsylvania , New Jersey and northern Delaware . We would like to see die signs using the old English letter M and royal blue colors. Also we stress WRSB compliance and safety.

Residential

Dalquist Construction Co Inc
1187 Harwick Lane
Birchfield PA 19448
Rolf Dalquist
rolf1dalquist@quillmail.net
267-555-0148

```html
<!DOCTYPE html>
<html lang="en">
<head>
<meta charset="utf-8">
<title>Dalquist Construction – Business Cards</title>
<link href="https://fonts.googleapis.com/css2?family=Jost:wght@400;500;700&display=swap" rel="stylesheet">
<style>
  :root {
    --navy: #1f2a6b;
    --card: #f8f6f1;
    --backdrop: #e6e4df;
    --ink: #26306f;
  }
  * { box-sizing: border-box; margin: 0; padding: 0; }
  html, body {
    width: 1029px;
    height: 1200px;
    overflow: hidden;
    background: var(--backdrop);
    font-family: "Jost", sans-serif;
    color: var(--navy);
  }
  .sheet {
    position: relative;
    width: 1029px;
    height: 1200px;
  }
  .card {
    position: absolute;
    left: 64px;
    width: 900px;
    height: 514px;
    background: var(--card);
    box-shadow: 0 6px 18px rgba(0,0,0,0.12);
  }
  .card--right-aligned { top: 48px; }
  .card--left-aligned { top: 622px; }

  .brand {
    position: absolute;
    left: 90px;
    top: 220px;
    width: 300px;
    display: flex;
    align-items: center;
    gap: 14px;
  }
  .brand__square {
    width: 26px;
    height: 26px;
    background: var(--navy);
    flex: none;
  }
  .brand__name {
    font-weight: 500;
    font-size: 30px;
    line-height: 1.1;
    color: var(--navy);
  }

  .divider {
    position: absolute;
    left: 400px;
    top: 110px;
    width: 3px;
    height: 300px;
    background: var(--navy);
  }

  .contact {
    position: absolute;
    color: var(--ink);
  }
  .contact__name {
    font-weight: 700;
    font-size: 46px;
    line-height: 1;
    margin-bottom: 12px;
  }
  .contact__line {
    font-size: 17px;
    line-height: 1.2;
  }
  .contact__row {
    display: flex;
    align-items: center;
    gap: 10px;
    font-size: 17px;
    line-height: 1.5;
  }
  .contact__gap { height: 16px; }
  .icon { width: 16px; height: 16px; flex: none; }

  .card--right-aligned .contact {
    right: 70px;
    top: 105px;
    text-align: right;
  }
  .card--right-aligned .contact__row { justify-content: flex-end; }

  .card--left-aligned .contact {
    left: 450px;
    top: 125px;
  }
  .card--left-aligned .contact__line,
  .card--left-aligned .contact__row { padding-left: 22px; }

  .tagline {
    position: absolute;
    right: 70px;
    bottom: 60px;
    font-size: 17px;
    color: var(--ink);
  }
</style>
</head>
<body>
<main class="sheet">

  <section class="card card--right-aligned">
    <div class="brand">
      <span class="brand__square"></span>
      <span class="brand__name">Dalquist Construction</span>
    </div>
    <div class="divider"></div>
    <div class="contact">
      <h1 class="contact__name">Rolf Dalquist</h1>
      <p class="contact__line">1187 Harwick Lane</p>
      <p class="contact__line">Birchfield PA 19448</p>
      <div class="contact__gap"></div>
      <p class="contact__row">rolf1dalquist@quillmail.net
        <svg class="icon" viewBox="0 0 18 18" aria-hidden="true"><rect x="1.5" y="4" width="15" height="10" fill="none" stroke="currentColor" stroke-width="1.6"/><path d="M1.5 4 9 10l7.5-6" fill="none" stroke="currentColor" stroke-width="1.6"/></svg>
      </p>
      <p class="contact__row">267-555-0148
        <svg class="icon" viewBox="0 0 18 18" aria-hidden="true"><rect x="5" y="1.5" width="8" height="15" rx="1.5" fill="none" stroke="currentColor" stroke-width="1.6"/><line x1="8" y1="14" x2="10" y2="14" stroke="currentColor" stroke-width="1.6"/></svg>
      </p>
    </div>
    <p class="tagline">WRSB compliance and SAFETY 1st</p>
  </section>

  <section class="card card--left-aligned">
    <div class="brand">
      <span class="brand__square"></span>
      <span class="brand__name">Dalquist Construction</span>
    </div>
    <div class="divider"></div>
    <div class="contact">
      <h2 class="contact__name">Rolf Dalquist</h2>
      <p class="contact__line">1187 Harwick Lane</p>
      <p class="contact__line">Birchfield PA 19448</p>
      <div class="contact__gap"></div>
      <p class="contact__row">
        <svg class="icon" viewBox="0 0 18 18" aria-hidden="true"><rect x="1.5" y="4" width="15" height="10" fill="none" stroke="currentColor" stroke-width="1.6"/><path d="M1.5 4 9 10l7.5-6" fill="none" stroke="currentColor" stroke-width="1.6"/></svg>
        rolf1dalquist@quillmail.net</p>
      <p class="contact__row">
        <svg class="icon" viewBox="0 0 18 18" aria-hidden="true"><rect x="5" y="1.5" width="8" height="15" rx="1.5" fill="none" stroke="currentColor" stroke-width="1.6"/><line x1="8" y1="14" x2="10" y2="14" stroke="currentColor" stroke-width="1.6"/></svg>
        267-555-0148</p>
    </div>
    <p class="tagline">WRSB compliance and SAFETY 1st</p>
  </section>

</main>
</body>
</html>
```